Medical Billing - Professional Marketing Flier

We are needing help designing a clean and professional looking easy to read marketing flier for a medical billing practice. The text needs to be large enough to print. We are looking for a 5.5 x 8.5 design that we can edit the text as needed. I have included our logo and what we initially want it to say. Please keep in mind, we also want our logo and contact details on the flier. Let me know if you have any questions.

```html
<!DOCTYPE html>
<html lang="en">
<head>
<meta charset="utf-8">
<title>Larkspur Medical Billing – Flier</title>
<link rel="stylesheet" href="https://fonts.googleapis.com/css2?family=Cinzel:wght@600&family=Arimo:wght@400&display=swap">
<style>
  :root{
    --page-bg:#c4e3f0;
    --white:#ffffff;
    --blue-light:#16a0d9;
    --blue-deep:#1a4790;
    --navy:#22367f;
    --violet:#5d4f9f;
    --pink:#c963a6;
    --purple:#7b5fad;
    --photo-light:#eef1f4;
    --photo-mid:#c7ced6;
    --body-size:17px;
  }
  *{margin:0;padding:0;box-sizing:border-box}
  html,body{width:960px;height:1200px;overflow:hidden;background:var(--page-bg)}
  .flier{position:absolute;left:92px;top:0;width:776px;height:1200px;background:var(--white);overflow:hidden;
    font-family:"Arimo",Arial,sans-serif;font-size:var(--body-size);line-height:21px}
  .flier__art{position:absolute;inset:0;width:776px;height:1200px}
  .brand{position:absolute;left:30px;top:84px;width:240px;text-align:center;
    font-family:"Arimo",Arial,sans-serif;font-weight:400;font-size:26px;line-height:32px;color:var(--navy)}
  .section-title{position:absolute;font-family:"Cinzel",serif;font-weight:600;font-size:31px;line-height:36px;letter-spacing:1px;white-space:nowrap}
  .copy{position:absolute;white-space:nowrap}
  .billing__title{left:26px;top:196px;color:var(--white)}
  .billing__copy{left:26px;top:238px;color:var(--white)}
  .aging__title{left:41px;top:522px;color:var(--violet)}
  .aging__copy{left:34px;top:574px;color:var(--navy)}
  .cred__title{left:404px;top:524px;color:var(--navy)}
  .cred__copy{left:404px;top:574px;color:var(--navy)}
  .contact__title{left:404px;top:903px;color:var(--white)}
  .contact__copy{left:404px;top:977px;color:var(--white)}
  .contact__details{left:34px;top:1063px;color:var(--white);font-style:normal}
</style>
</head>
<body>
<main class="flier">
  <svg class="flier__art" viewBox="0 0 776 1200">
    <defs>
      <linearGradient id="bandBlue" x1="0" y1="0" x2="1" y2="0">
        <stop offset="0" stop-color="var(--blue-light)"/><stop offset="0.6" stop-color="var(--blue-deep)"/>
      </linearGradient>
      <linearGradient id="cornerBlue" x1="0" y1="0" x2="0" y2="1">
        <stop offset="0" stop-color="var(--blue-light)"/><stop offset="0.7" stop-color="var(--blue-deep)"/>
      </linearGradient>
      <linearGradient id="photoTone" x1="0" y1="0" x2="1" y2="1">
        <stop offset="0" stop-color="var(--photo-mid)"/><stop offset="0.5" stop-color="var(--photo-light)"/><stop offset="1" stop-color="#dfe4ea"/>
      </linearGradient>
      <linearGradient id="barTone" x1="0" y1="0" x2="1" y2="0">
        <stop offset="0" stop-color="#1a55a0"/><stop offset="1" stop-color="#1ca0d8"/>
      </linearGradient>
      <linearGradient id="purpleTone" x1="0" y1="0" x2="1" y2="0">
        <stop offset="0.3" stop-color="var(--pink)"/><stop offset="1" stop-color="var(--purple)"/>
      </linearGradient>
    </defs>

    <rect class="band" x="0" y="177" width="776" height="331" fill="url(#bandBlue)"/>
    <path class="photo-frame" d="M296,0 H776 V494 C590,492 430,420 360,250 C325,170 305,90 296,0 Z" fill="var(--white)"/>
    <path class="photo" role="img" aria-label="Photo of a stethoscope, thermometer, pills and a chart on a desk"
          d="M304,0 H776 V476 C600,474 440,402 370,244 C336,168 314,88 304,0 Z" fill="url(#photoTone)"/>
    <g class="bars" fill="url(#barTone)" opacity="0.9">
      <rect x="658" y="44" width="118" height="12"/>
      <rect x="576" y="104" width="200" height="12"/>
      <rect x="507" y="168" width="269" height="12"/>
      <rect x="507" y="229" width="269" height="12"/>
      <rect x="530" y="290" width="246" height="12"/>
      <rect x="600" y="343" width="176" height="12"/>
      <rect x="518" y="402" width="258" height="12"/>
    </g>

    <path class="corner-blue" d="M0,832 C130,824 245,872 292,985 C316,1045 322,1125 322,1200 H0 Z" fill="url(#cornerBlue)"/>
    <path class="corner-purple" d="M776,700 C745,790 660,822 540,838 C420,854 334,904 304,972 C288,1042 316,1130 339,1200 H776 Z"
          fill="url(#purpleTone)" stroke="var(--white)" stroke-width="10"/>
  </svg>

  <div class="brand">Larkspur<br>Medical Billing</div>

  <h2 class="section-title billing__title">MEDICAL BILLING</h2>
  <p class="copy billing__copy">Would you prefer to spend time<br>focusing on your clients and running<br>your practice rather than trying to stay<br>up to speed with the constantly<br>changing medical billing rules and<br>regulations? Let us help you by<br>managing your medical billing and dealing<br>with the insurance companies on your<br>behalf! We work with you to tailor the entire<br>medical billing process to suit your practices<br>needs while making it as smooth and<br>painless as possible.</p>

  <h2 class="section-title aging__title">AGING</h2>
  <p class="copy aging__copy">Are you leaving money on the table?<br>Are you able to do the follow-through<br>needed to keep your aging in check<br>and more money flowing into your<br>practice? Are you uncertain about<br>how to get insurance to pay on claims<br>that should be covered but for some<br>reason they decided not to? We can<br>clean up your aging, reduce the<br>amount of time it takes for claims to<br>pay out, and we can keep your aging<br>to a minimum.</p>

  <h2 class="section-title cred__title">CREDENTIALING</h2>
  <p class="copy cred__copy">Are you wanting to get contracted<br>with insurance companies but aren’t<br>sure how to go about it? Are you<br>wanting to expand your client base by<br>having the option to bill insurance?<br>Let us take the confusion out of what<br>can seem like a daunting task! We<br>can get you and your practitioners<br>contracted with the insurance<br>companies of your choice and help<br>you navigate through the process<br>every step of the way!</p>

  <h2 class="section-title contact__title">CONTACT US</h2>
  <p class="copy contact__copy">If any of these processes are something you<br>would like our help with or to consult with<br>us on, please email us or give us a call! We<br>specialize in billing and contracting for<br>Nutritionists and Dietitians. We would love<br>to help you expand your business and take<br>the pain and frustration out of billing so you<br>can focus on your clients.</p>

  <address class="copy contact__details">
    Address: PO Box 418 Cedar Falls,<br>
    WA 98010<br>
    Phone: 555-014-2270<br>
    Email:<br>
    admin@larkspurbilling.com
  </address>
</main>
</body>
</html>
```